Aviation security consulting company needs a website

We need a website design for Brisk Holloway, and aviation security consulting company. Brisk Holloway (www.briskholloway.example) is an aviation security consulting company that works with government and industry stakeholders in over 60 countries on aviation security strategy, governance, and oversight at the regulatory and operational level.
Brisk Holloway is strongly internationally focused.
The website required should be simple, corporate, serious, and communicate professionalism, reliability and honesty. We are trying to give the company a feeling of being well established.
The attached files include the company logo, along with examples of company web page styles that we like.
The Brisk Holloway website need only be around five pages long (landing page, who we are, our services, our clients, contact), though don't feel limited to only five pages.
The existing website (www.briskholloway.example) was rushed and put together using Wix. We don't love the existing website as it looks too amateur, so don't use it as a template.
There is no requirement for any online sales tools to be included in the site. The site is purely informational, with the option of people making contact via email.

```html
<!DOCTYPE html>
<html lang="en">
<head>
<meta charset="utf-8">
<title>Brisk Holloway – Our Services</title>
<link href="https://fonts.googleapis.com/css2?family=Raleway:wght@400;500;600;700&display=swap" rel="stylesheet">
<style>
  :root {
    --navy: #1b2d6b;
    --ink: #111111;
    --white: #ffffff;
    --rule: #8a8a8a;
    --band: rgba(10, 10, 12, 0.88);
  }
  * { margin: 0; padding: 0; box-sizing: border-box; }
  html, body { width: 1200px; height: 1173px; overflow: hidden; background: var(--white); }
  body { font-family: "Raleway", Arial, sans-serif; color: var(--ink); position: relative; }

  .site-header { position: absolute; top: 0; left: 0; width: 1200px; height: 96px; }
  .brand { position: absolute; left: 95px; top: 15px; display: flex; align-items: center; gap: 12px; }
  .brand-mark { width: 66px; height: 66px; background: var(--navy); }
  .brand-text { display: flex; flex-direction: column; }
  .brand-name { font-size: 35px; font-weight: 700; color: var(--navy); line-height: 1; letter-spacing: -0.3px; white-space: nowrap; }
  .brand-tagline { font-size: 15px; font-weight: 500; color: var(--navy); letter-spacing: 2.2px; margin-top: 4px; white-space: nowrap; }

  .main-nav { position: absolute; right: 78px; top: 0; display: flex; height: 71px; }
  .main-nav a { display: block; padding: 40px 15px 0; font-size: 14px; color: var(--ink); text-decoration: none; height: 71px; white-space: nowrap; }
  .main-nav a.is-active { background: var(--navy); color: var(--white); padding: 40px 12px 0; }

  .hero { position: absolute; top: 96px; left: 0; width: 1200px; height: 340px;
    background: linear-gradient(180deg, #a9c3d8 0%, #d6dde2 30%, #8b9198 52%, #2b2d31 70%, #1a1b1e 100%); }
  .hero-caption { position: absolute; left: 0; bottom: 0; width: 100%; height: 116px; background: var(--band);
    color: var(--white); text-align: center; font-size: 18px; font-weight: 400; line-height: 22px; padding-top: 32px; white-space: nowrap; }

  .service { position: absolute; width: 408px; }
  .service.is-right { width: 402px; }
  .service h2 { font-size: 20.5px; font-weight: 600; color: var(--navy); line-height: 24px; margin-bottom: 4px; white-space: nowrap; }
  .service.is-spaced h2 { margin-bottom: 8px; }
  .service p { font-size: 13px; line-height: 15.6px; }
  .service ul { list-style: none; margin-top: 13px; padding-left: 14px; }
  .service li { font-size: 13px; line-height: 15.6px; position: relative; padding-left: 18px; white-space: nowrap; }
  .service li::before { content: ""; position: absolute; left: 0; top: 5px; border-left: 5px solid var(--ink);
    border-top: 3px solid transparent; border-bottom: 3px solid transparent; }

  .site-footer { position: absolute; top: 1120px; left: 0; width: 1200px; border-top: 1px solid var(--rule); }
  .copyright { position: absolute; left: 96px; top: 23px; font-size: 11px; white-space: nowrap; }
  .footer-links { position: absolute; right: 94px; top: 22px; font-size: 11px; white-space: nowrap; }
</style>
</head>
<body>
  <header class="site-header">
    <div class="brand">
      <div class="brand-mark"></div>
      <div class="brand-text">
        <span class="brand-name">Brisk Holloway</span>
        <span class="brand-tagline">aviation security consulting</span>
      </div>
    </div>
    <nav class="main-nav">
      <a href="#">Home</a>
      <a href="#">Who We Are</a>
      <a href="#" class="is-active">Our Services</a>
      <a href="#">Our Clients</a>
      <a href="#">Contact</a>
    </nav>
  </header>

  <section class="hero" role="img" aria-label="Photo of an airport departure lounge with rows of seats facing a parked airliner through large windows">
    <div class="hero-caption">In depth knowledge built through years of experience brings the ability to deliver<br>expertise to all areas of aviation security for industry and government stakeholders.</div>
  </section>

  <article class="service is-spaced" style="left:129px; top:516px;">
    <h2>Civil Aviation Authority / Regulator</h2>
    <p>Aviation security regulatory agencies are required to navigate a plethora of conflicting domestic regulation, along with regional and international aviation security requirements.<br>In addition, civil aviation authorities are required to ensure these regulations are appropriately implemented at the national level. Brisk Holloway can assist by, inter alia, developing regulation and other regulatory mechanisms, training national inspectors, and developing audit and compliance assessment tools and programs.</p>
  </article>

  <article class="service is-right is-spaced" style="left:649px; top:518px;">
    <h2>Airport Operations and Screening</h2>
    <p>Brisk Holloway can work with airports and airport designers to ensure security is incorporated in airport designs, and is maximised within existing airport environments. Services include:</p>
    <ul>
      <li>Passenger screening point design and efficiency</li>
      <li>audit and inspection of processes</li>
      <li>access and egress</li>
      <li>airport security management</li>
      <li>vulnerability assessments (including front of house design)</li>
    </ul>
  </article>

  <article class="service" style="left:129px; top:736px;">
    <h2>Air Cargo / Handling Agent</h2>
    <p>Air cargo security is seeing rapid changes, with issues such as pre-loading advanced cargo information, electronic consignment security declarations, and secure supply chains becoming more important. Regulators continue to move away from 100% screening at airports towards whole of supply chain approaches incorporating more industry stakeholders.<br>Brisk Holloway can assist air cargo operators meet aviation security obligations while ensuring facilitation and profitability are maintained.</p>
  </article>

  <article class="service is-right" style="left:649px; top:736px;">
    <h2>Capacity Development</h2>
    <p>Every country is different, and while States must meet the same international standards, there is no 'one size fits all' approach. Each State must develop solutions that are sustainable in their economies.<br>Brisk Holloway has extensive experience working in partnership with developing economies to implement incremental changes to aviation security that don't just meet immediate needs, but maintain their viability over the medium and long term.</p>
  </article>

  <article class="service" style="left:129px; top:944px;">
    <h2>Airline</h2>
    <p>Brisk Holloway can work with airlines on security issues such as security program development, station inspection and audit, strategic guidance, and change management.</p>
  </article>

  <article class="service is-right" style="left:651px; top:931px;">
    <h2>Training</h2>
    <p>Brisk Holloway has experienced aviation security trainers who can take participants through course material prepared by your organisation, or can develop training material tailored to your requirements.</p>
  </article>

  <footer class="site-footer">
    <div class="copyright">© 2016. Brisk Holloway. All Rights Reserved.</div>
    <div class="footer-links">Terms &nbsp;|&nbsp;&nbsp; Privacy Policy</div>
  </footer>
</body>
</html>
```